Business Card Design for Animal Clinic

We are seeking a two sided business card design. The primary side should include our logo (provided in AI and EPS files) address, phone, website, and if possible "Follow Us" with icons for Facebook, Google+, and Twitter.

The back of the card needs to included space for appointment reminders.

Company Name:
Brackenfield Animal Clinic

Doctor Name:
To be provided to winner

Adress:
To be provided to winner

Phone:
to be provided to winner

Website:
www.brackenfieldanimalclinic.example

```html
<!DOCTYPE html>
<html lang="en">
<head>
<meta charset="utf-8">
<title>Brackenfield Animal Clinic – Business Card</title>
<link rel="stylesheet" href="https://fonts.googleapis.com/css2?family=Arimo:wght@400&display=swap">
<style>
  :root {
    --page-bg: #e8e4df;
    --card-black: #0f0d0d;
    --card-glow: #4a211d;
    --brand-red: #b3262b;
    --rule-red: #a3272a;
    --text-soft: #b9a3a0;
    --decor-tone: #2a1b1a;
    --decor-edge: #3a2523;
  }
  * { box-sizing: border-box; margin: 0; padding: 0; }
  html, body {
    width: 1200px; height: 900px; overflow: hidden;
    background: var(--page-bg);
    font-family: "Arimo", Arial, sans-serif;
  }
  .canvas { position: relative; width: 1200px; height: 900px; }

  .card {
    position: absolute; left: 327px; width: 546px; height: 293px;
    border-radius: 4px; overflow: hidden;
    background:
      radial-gradient(ellipse 60% 70% at 50% 100%, var(--card-glow) 0%, rgba(74,33,29,0.35) 45%, transparent 80%),
      var(--card-black);
    box-shadow: 0 3px 10px rgba(0,0,0,0.25);
  }
  .card--front { top: 111px; }
  .card--back  { top: 443px; }

  .cat-decor {
    position: absolute; top: 23px; width: 62px; height: 266px;
    background: linear-gradient(180deg, var(--decor-edge) 0%, var(--decor-tone) 60%, transparent 100%);
    border-radius: 30px 30px 0 0;
    opacity: 0.7;
  }
  .card--front .cat-decor { right: 0; }
  .card--back .cat-decor  { left: 0; }

  .brand {
    position: absolute; left: 0; right: 0; top: 44px;
    display: flex; align-items: center; justify-content: center; gap: 14px;
  }
  .brand__mark {
    width: 18px; height: 18px; border-radius: 50%;
    background: var(--brand-red);
  }
  .brand__name {
    color: var(--brand-red);
    font-size: 40px; font-weight: 400; letter-spacing: 2px;
    text-transform: uppercase; line-height: 1.15; text-align: center;
  }

  .rule {
    position: absolute; left: 0; right: 0; top: 210px; height: 2px;
    background: var(--rule-red);
  }

  .contact {
    position: absolute; left: 0; right: 0; top: 223px;
    text-align: center; line-height: 21px;
  }
  .contact__address { color: var(--text-soft); font-size: 17px; }
  .contact__phone {
    color: var(--text-soft); font-size: 17px;
    display: inline-flex; align-items: center; gap: 8px;
  }
  .contact__phone svg { width: 17px; height: 17px; }
  .contact__web { color: var(--rule-red); font-size: 17px; display: block; }
</style>
</head>
<body>
<main class="canvas">
  <section class="card card--front" aria-label="Business card front">
    <div class="cat-decor" role="img" aria-label="Faint cat silhouette decoration along the right edge"></div>
    <div class="brand">
      <span class="brand__mark"></span>
      <h1 class="brand__name">Brackenfield<br>Animal Clinic</h1>
    </div>
    <div class="rule"></div>
    <div class="contact">
      <p class="contact__address">418 N. Larchmere Avenue, Fernbrook Springs, FL 32990</p>
      <p class="contact__phone">
        <svg viewBox="0 0 20 20" aria-hidden="true">
          <circle cx="10" cy="10" r="9.5" fill="#2b2222"/>
          <path d="M6.5 5.2c.5-.4 1.1-.3 1.4.2l1 1.6c.3.5.2 1-.2 1.3l-.7.6c.5 1.2 1.4 2.2 2.6 2.7l.6-.7c.4-.4.9-.5 1.3-.2l1.6 1c.5.3.6.9.2 1.4l-.7.8c-.5.5-1.3.7-2 .4-2.6-1-4.7-3.1-5.7-5.7-.3-.7-.1-1.5.4-2z" fill="#8a7775"/>
        </svg>
        (555) 014 - 2286
      </p>
      <a class="contact__web">www.brackenfieldanimalclinic.example</a>
    </div>
  </section>

  <section class="card card--back" aria-label="Business card back">
    <div class="cat-decor" role="img" aria-label="Faint cat silhouette decoration along the left edge"></div>
  </section>
</main>
</body>
</html>
```